Singer/Song Writer on a Spirited Path needs Album Cover Design

I'm looking for a design for my Album titled: The Lantern Hour.
I would like to steer it away from the strictly "Christian" eschatology of "the Lantern Hour" and into the direction of these definitions of Rapture...
"intense bliss or beatitude"
"powerful emotion that lifts one out of oneself"
"a state or feeling of great happiness, pleasure, or love"

The 1st song on my album is named "Carry The Stone" And there's also a song titled "The Heron" to which the chorus is: "Consume me and free The Heron"
The album is compiled of songs about life's stuggles and triumphs/ pain and beauty/ ups and downs... with hopefully helpful words and sounds to ease our human condition.

I envision something like a Phoenix rising from the waters of life. But I don't want it to be too literally a Phoenix. I like The Heron as flames and not extremely birdlike. I like The Heron in file #1 the best... but like the half water, half phoenix in File 2.
The other 2 files are just to give some more ideas I've had that might be incorporated.
Thanks!

Reason: I needed a little more time, as I am sharing my project with my producer and my family... both of whom are out of the country. Thank you!

Other font styles liked:
• Depending on the design... I like 'Many Weatz' or 'Anaema' or 'Before the Rain' for the album title... "The Lantern Hour"

• My name: "Liesel"
• The album title: "The Lantern Hour"
• Not sure where this should appear:
• Produced/recorded at 'The Vault' in Montezuma, Costa Rica, with/by Ferrante

```html
<!DOCTYPE html>
<html lang="en">
<head>
<meta charset="utf-8">
<title>Liesel — The Lantern Hour</title>
<link rel="stylesheet" href="https://fonts.googleapis.com/css2?family=Josefin+Sans:wght@300&family=Great+Vibes&display=swap">
<style>
  :root {
    --paper: #ffffff;
    --ink: #111111;
    --flame-gold: #f7b52a;
    --flame-orange: #f07a2c;
    --flame-red: #e2392f;
    --water-blue: #2a9fdc;
    --water-deep: #1a78c2;
  }
  html, body {
    margin: 0;
    padding: 0;
    width: 1200px;
    height: 1200px;
    overflow: hidden;
    background: var(--paper);
  }
  .album-cover {
    position: relative;
    width: 1200px;
    height: 1200px;
    background: var(--paper);
    overflow: hidden;
  }
  .cover-artwork {
    position: absolute;
    left: 0;
    top: 0;
    width: 1200px;
    height: 1200px;
  }
  .artist-name {
    position: absolute;
    top: 22px;
    left: 0;
    width: 1200px;
    margin: 0;
    display: flex;
    justify-content: center;
    gap: 118px;
    font-family: "Josefin Sans", sans-serif;
    font-weight: 300;
    font-size: 104px;
    line-height: 1;
    color: var(--ink);
    padding-left: 14px;
    box-sizing: border-box;
  }
  .album-title {
    position: absolute;
    top: 178px;
    left: 0;
    width: 1200px;
    margin: 0;
    text-align: center;
    font-family: "Great Vibes", cursive;
    font-weight: 400;
    font-size: 118px;
    line-height: 1;
    color: var(--ink);
  }
</style>
</head>
<body>
  <main class="album-cover">
    <svg class="cover-artwork" viewBox="0 0 1200 1200" role="img"
         aria-label="Illustration of a heron formed from golden and red flames with spreading wings, rising out of a glowing blue sphere of splashing water">
      <defs>
        <linearGradient id="fire-to-water" x1="0" y1="0" x2="0" y2="1">
          <stop offset="0" stop-color="var(--flame-gold)" stop-opacity="0.35"/>
          <stop offset="0.35" stop-color="var(--flame-gold)"/>
          <stop offset="0.6" stop-color="var(--flame-orange)"/>
          <stop offset="0.78" stop-color="var(--flame-red)"/>
          <stop offset="0.86" stop-color="var(--water-blue)"/>
          <stop offset="1" stop-color="var(--water-deep)"/>
        </linearGradient>
        <radialGradient id="soft-edge" cx="0.5" cy="0.6" r="0.55">
          <stop offset="0.55" stop-color="#fff" stop-opacity="1"/>
          <stop offset="1" stop-color="#fff" stop-opacity="0"/>
        </radialGradient>
        <mask id="artwork-fade">
          <rect x="0" y="0" width="1200" height="1200" fill="url(#soft-edge)"/>
        </mask>
      </defs>
      <rect x="120" y="110" width="960" height="1090" fill="url(#fire-to-water)" mask="url(#artwork-fade)"/>
    </svg>

    <h1 class="artist-name" aria-label="Liesel">
      <span>L</span><span>I</span><span>E</span><span>S</span><span>E</span><span>L</span>
    </h1>
    <h2 class="album-title">The Lantern Hour</h2>
  </main>
</body>
</html>
```